Renewable Energy company needs a new website

We are renewable energy company that has been operating for 3 years now and require a new website design. We are looking to upgrade our website to be comparable to our competitors. We are not a brick and mortar business so our website does need to be very appealing and convey a sense of authenticity and trust to the consumer. It will also heavily display our current system special and offering etc. The final design needs to be visually appealing in a marketing sense however also needs to convey a high sense of professionalism.

Target Market(s)

Consumers of solar systems for installation on their home or business.

Coding

Coded - Design and coding required

Number of Pages Required

3 page

Font styles to use
Sans Serif

Colors

Designer to choose colors to be used in the design.

Requirements
Must have
• A home page, a page for residential solar systems including the packages we are currently offering and a commercial page for larger installations of solar systems.
• www.torvapower.com.au
Nice to have
• As a template we do like this https://www.bluneklight.com.au/qld/ in terms of design elements and layout of the page.

```html
<!DOCTYPE html>
<html lang="en">
<head>
<meta charset="utf-8">
<title>Torva Power — Solar Energy Solutions</title>
<link href="https://fonts.googleapis.com/css2?family=Roboto+Condensed:wght@700&family=Lato:wght@400;700&family=PT+Serif:wght@400;700&display=swap" rel="stylesheet">
<style>
:root{
  --red:#c41e2f;
  --red-dark:#a5162a;
  --red-soft:#d04150;
  --pink:#fbeef0;
  --grey:#efefef;
  --ink:#1e1e1e;
  --text:#555;
  --white:#fff;
}
*{box-sizing:border-box;margin:0;padding:0}
html,body{width:1200px;height:5236px;overflow:hidden}
body{position:relative;background:var(--white);font-family:"Lato",sans-serif;color:var(--text)}
.abs{position:absolute}
.btn{position:absolute;display:flex;align-items:center;justify-content:center;background:var(--red);color:var(--white);font-family:"PT Serif",serif;font-weight:700;font-size:16px;letter-spacing:.5px;border-radius:4px;text-transform:uppercase}
.heading{font-family:"PT Serif",serif;font-weight:700;color:var(--ink);text-transform:uppercase;letter-spacing:.5px}
.heading em{font-style:normal;color:var(--red)}
.photo{position:absolute}
/* header */
.brand{position:absolute;display:flex;align-items:center;gap:10px;font-family:"Lato",sans-serif;font-weight:700;font-size:26px;color:var(--ink)}
.brand .mark{width:22px;height:22px;background:var(--red)}
.nav{position:absolute;left:412px;top:36px;display:flex;gap:20px;font-size:14px;color:var(--ink);text-transform:uppercase}
.nav .active{color:var(--red)}
.nav .active::before{content:"•";margin-right:6px}
.phone{position:absolute;left:810px;top:28px;display:flex;align-items:center;gap:8px;font-family:"Roboto Condensed",sans-serif;font-size:22px;color:var(--ink)}
/* hero */
.hero-title{left:78px;top:205px;font-family:"Roboto Condensed",sans-serif;font-size:42px;line-height:50px;color:var(--ink)}
.hero-copy{left:78px;top:322px;width:400px;font-size:16px;line-height:27px;color:#444}
.hero-copy b{color:var(--red)}
/* features */
.features{left:0;top:677px;width:1200px;height:323px;display:flex;background:var(--red)}
.feature{flex:1;display:flex;flex-direction:column;align-items:center;text-align:center;color:var(--white)}
.feature:nth-child(odd){background:var(--red-dark)}
.feature .icon{margin-top:62px;width:98px;height:98px;border-radius:10px;background:var(--white);display:flex;align-items:center;justify-content:center}
.feature h3{margin-top:28px;font-family:"PT Serif",serif;font-size:17px;line-height:22px;text-transform:uppercase;height:46px}
.feature p{margin-top:12px;font-size:14px;color:#f5d0d4}
/* plug */
.plug-copy{left:155px;top:1128px;width:395px;font-size:13px;line-height:27px;color:#555}
.plug-copy p+p{margin-top:20px}
.tag{position:absolute;background:var(--red);color:var(--white);font-family:"PT Serif",serif;font-weight:700;font-size:15px;display:flex;align-items:center;justify-content:center}
/* why */
.why-list{left:660px;top:1770px;width:463px}
.why-list li{list-style:none;height:62px;margin-bottom:22px;background:var(--red-soft);border-left:3px solid var(--white);color:var(--white);font-family:"PT Serif",serif;font-size:16px;display:flex;align-items:center;padding-left:33px}
.why-list li.on{background:var(--red-dark)}
/* form */
.field{position:absolute;height:50px;background:var(--white);font-size:12px;color:#777;padding:18px 14px}
.field.active{background:var(--red-soft);color:var(--white)}
/* packages */
.card{position:absolute;top:3820px;width:342px;height:685px;background:var(--white);box-shadow:0 0 14px rgba(0,0,0,.08)}
.card .top{height:150px;background:var(--pink);display:flex;align-items:center;justify-content:center;text-align:center;font-family:"PT Serif",serif;font-weight:700;font-size:22px;line-height:30px;color:var(--ink)}
.card .badge{position:absolute;left:139px;top:120px;width:62px;height:58px;background:var(--red)}
.card .badge::after{content:"";position:absolute;inset:14px;border:3px solid var(--white)}
.card .desc{position:absolute;left:20px;right:20px;font-size:13px;line-height:27px;text-align:center;color:#666}
.card ul{position:absolute;left:62px;list-style:none;font-size:14px;line-height:27px;color:var(--ink)}
.card li{display:flex;gap:12px;margin-bottom:16px}
.card li::before{content:"✔";color:var(--red)}
/* footer */
.foot-h{position:absolute;font-family:"PT Serif",serif;font-weight:700;font-size:16px;color:var(--ink);text-transform:uppercase}
.foot-list{position:absolute;list-style:none;font-size:13px;line-height:29px;color:#666}
.foot-list li::before{content:"•";color:var(--red);margin-right:14px}
.foot-txt{position:absolute;font-size:13px;line-height:26px;color:#666}
</style>
</head>
<body>

<!-- Header -->
<header>
  <div class="brand" style="left:76px;top:30px"><span class="mark"></span>Torva Power</div>
  <nav class="nav"><span class="active">Home</span><span>Residential</span><span>Commercial</span><span>Off-Grid</span></nav>
  <div class="phone">
    <svg width="24" height="24" viewBox="0 0 24 24"><circle cx="12" cy="12" r="10.5" fill="none" stroke="#c41e2f" stroke-width="2"/><path d="M9 7l2 3-1.3 1.2a7 7 0 003 3L14 13l3 2-1 2c-4 0-9-5-9-9z" fill="#c41e2f"/></svg>
    (07) 3040 8812
  </div>
  <div class="btn" style="left:985px;top:22px;width:138px;height:46px;font-size:15px">Free Quote</div>
</header>

<!-- Hero -->
<section class="hero">
  <svg class="abs" style="left:0;top:80px" width="1200" height="597" viewBox="0 0 1200 597">
    <path d="M0 470 C 200 470 300 520 480 560 L 560 597 L 0 597 Z" fill="#fbeef0"/>
    <path d="M560 597 C 700 500 760 160 1000 80 C 1100 40 1160 0 1200 0 L 1200 597 Z" fill="#fbeef0"/>
  </svg>
  <h1 class="abs hero-title">Tired Of The Power Bill<br>Getting Larger Each Year?</h1>
  <p class="abs hero-copy">you save <b>up to 80%</b> on your energy costs through our effective and efficient energy management systems!</p>
  <div class="btn" style="left:76px;top:420px;width:199px;height:53px">Get Free Quote</div>
  <svg class="photo" style="left:395px;top:255px" width="750" height="422" viewBox="0 0 750 422" role="img" aria-label="Smiling family in front of a house with solar panels on the roof">
    <defs><linearGradient id="heroG" x1="0" y1="0" x2="1" y2="1"><stop offset="0" stop-color="#d9c6a6"/><stop offset=".5" stop-color="#a9b5c4"/><stop offset="1" stop-color="#6b7f97"/></linearGradient></defs>
    <path d="M120 160 C 180 60 330 20 470 30 C 640 40 750 120 745 240 C 740 360 640 422 520 422 L 90 422 C 20 400 0 340 20 280 C 40 230 80 210 120 160 Z" fill="url(#heroG)"/>
  </svg>
</section>

<!-- Service features -->
<section class="abs features">
  <div class="feature"><div class="icon"><svg width="56" height="44" viewBox="0 0 56 44"><g fill="none" stroke="#333" stroke-width="2"><circle cx="14" cy="18" r="6"/><path d="M24 10h26l-4 24H20zM30 10l-3 24M40 10l-3 24M22 22h26"/><path d="M14 4v4M4 18h4M6 10l3 3M6 26l3-3"/></g></svg></div><h3>Commercial<br>Solar Power</h3><p>Reduce Costs, Grow Your Business</p></div>
  <div class="feature"><div class="icon"><svg width="60" height="30" viewBox="0 0 60 30"><rect x="2" y="2" width="56" height="26" rx="13" fill="none" stroke="#333" stroke-width="2.5"/><circle cx="43" cy="15" r="8" fill="none" stroke="#333" stroke-width="2.5"/></svg></div><h3>Off Grid Power</h3><p>Avoid Blackouts, Go Off-Grid</p></div>
  <div class="feature"><div class="icon"><svg width="50" height="50" viewBox="0 0 50 50"><g fill="none" stroke="#333" stroke-width="2"><path d="M10 20h30l-4 24H14z"/><path d="M18 20l2 24M26 20v24M34 20l-2 24"/><circle cx="36" cy="10" r="5"/><path d="M36 2v2M44 10h2M42 4l2-2"/></g></svg></div><h3>Solar Water<br>Pumps</h3><p>Go Solar, Eliminate Fuel Cost</p></div>
  <div class="feature"><div class="icon"><svg width="50" height="50" viewBox="0 0 50 50"><g fill="none" stroke="#333" stroke-width="2"><path d="M6 46V24l19-12 19 12v22z"/><rect x="19" y="4" width="12" height="12"/><path d="M14 30h6v6h-6zM30 30h6v6h-6zM22 46V36h6v10"/></g></svg></div><h3>Residential Solar<br>Power</h3><p>Save Money For Your Family</p></div>
</section>

<!-- Plug into the sun -->
<section class="plug">
  <h2 class="abs heading" style="left:155px;top:1065px;font-size:38px;font-weight:400">Plug <em>into the</em> Sun</h2>
  <div class="abs plug-copy">
    <p>At Torva Power, we believe that you deserve better. Poor services and huge costs for electricity don't sit well with us. That's why we do our best to provide our clients with up-to-date energy management systems that can immediately result to significant reductions in their electricity expenses.</p>
    <p>Solar power is still one of the best ways to cut down on your monthly energy bills. So with the fast growing trend of organizations adopting commercial solar energy solutions, we will provide you with viable options that are tailored-fit for your needs. Gain control of your energy usage. Plug into the sun and go solar now!</p>
  </div>
  <div class="btn" style="left:158px;top:1488px;width:162px;height:52px">Learn More</div>
  <div class="photo" role="img" aria-label="Blue house with solar panels on the roof" style="left:620px;top:1063px;width:365px;height:219px;background:linear-gradient(160deg,#9ec3e6,#3b5a86 60%,#2a3b55)"></div>
  <div class="tag" style="left:786px;top:1232px;width:199px;height:50px">RESIDETIAL SOLAR</div>
  <div class="photo" role="img" aria-label="Rows of solar panels in front of a city skyline" style="left:685px;top:1305px;width:363px;height:219px;background:linear-gradient(170deg,#bcd9f2,#4d79b1 55%,#6d9a5a)"></div>
  <div class="tag" style="left:848px;top:1474px;width:200px;height:50px">COMMERCIAL SOLAR</div>
</section>

<!-- Why go solar -->
<section class="why">
  <div class="photo" role="img" aria-label="Installers fitting solar panels on a house roof" style="left:0;top:1607px;width:600px;height:488px;background:linear-gradient(165deg,#cfe4f5,#8fb6d8 40%,#2f5b8e 70%,#4a4a4a)"></div>
  <div class="abs" style="left:0;top:2095px;width:600px;height:187px;background:var(--grey)"></div>
  <svg class="abs" style="left:76px;top:2045px" width="96" height="96" viewBox="0 0 96 96"><circle cx="48" cy="48" r="46" fill="#fff"/><g fill="none" stroke="#c41e2f" stroke-width="2.5"><path d="M36 40l12-7 12 7v16l-12 7-12-7z"/><path d="M36 40l12 7 12-7M48 47v16"/><path d="M48 24v8M44 28l4-4 4 4"/></g></svg>
  <p class="abs" style="left:78px;top:2142px;width:480px;font-size:14px;line-height:27px;color:#555">Gone are the days when the only way to use electricity is through the grid. Now, you don't have to suffer from expensive electricity costs and terrible service. You now have the power to go off-grid and reduce your electricity costs!</p>
  <div class="abs" style="left:600px;top:1607px;width:600px;height:675px;background:var(--red)"></div>
  <h2 class="abs heading" style="left:663px;top:1658px;font-size:34px;line-height:47px;color:var(--white);font-weight:400">Why do you need<br>to go solar ?</h2>
  <ul class="abs why-list">
    <li>Get Consistent Savings for 20+ Years</li>
    <li class="on">Be Independent from The Grid</li>
    <li>Increase and Maximise Your Bottomline</li>
    <li>Differentiate Your Business Against Competitors</li>
    <li>Take Part in Solving Global Warming</li>
  </ul>
</section>

<!-- Savings -->
<section class="save">
  <h2 class="abs heading" style="left:0;top:2348px;width:1200px;text-align:center;font-size:34px;line-height:47px;font-weight:400">BrightPath cut <em>80% off</em><br>their power bill</h2>
  <svg class="photo" style="left:165px;top:2478px" width="415" height="370" viewBox="0 0 415 370" role="img" aria-label="Collage of solar panels at sunset, rooftop panels and a green landscape">
    <defs><linearGradient id="dA" x1="0" y1="0" x2="0" y2="1"><stop offset="0" stop-color="#f1c48a"/><stop offset="1" stop-color="#6d5b4a"/></linearGradient><linearGradient id="dB" x1="0" y1="0" x2="1" y2="1"><stop offset="0" stop-color="#9cc3e8"/><stop offset="1" stop-color="#2e56a0"/></linearGradient><linearGradient id="dC" x1="0" y1="0" x2="1" y2="1"><stop offset="0" stop-color="#d9ebc0"/><stop offset="1" stop-color="#4f8a3a"/></linearGradient></defs>
    <path d="M208 0 L300 92 L208 184 L116 92Z" fill="url(#dA)"/>
    <path d="M92 122 L184 214 L92 306 L0 214Z" fill="url(#dB)"/>
    <path d="M322 122 L414 214 L322 306 L230 214Z" fill="url(#dC)"/>
    <path d="M208 240 L300 332 L208 370 L116 332Z" fill="url(#dB)"/>
  </svg>
  <div class="abs" style="left:653px;top:2516px;width:350px;font-size:14px;line-height:29px;color:#555">
    <p>Whether you're a huge commercial establishment or a small property owner, Torva Power has the perfect solution to give you consistent savings on your monthly bills.</p>
    <p style="margin-top:16px">Get your <b style="color:var(--ink)">FREE Quote</b> and discover how you can save thousands of dollars from reduced energy cost by choosing to go solar!</p>
  </div>
  <div class="btn" style="left:653px;top:2763px;width:162px;height:50px">Free Quote</div>
  <div class="photo" role="img" aria-label="Illustration of solar panel rows on grass with a transmission tower" style="left:0;top:2888px;width:1200px;height:238px;background:linear-gradient(180deg,#fff 0%,#f2f2f2 60%,#9bd04a 88%,#6cb52c 100%)"></div>
</section>

<!-- Quote form -->
<section class="abs" style="left:0;top:3126px;width:1200px;height:352px;background:var(--red)">
  <h2 class="abs heading" style="left:0;top:58px;width:1200px;text-align:center;color:var(--white);font-size:36px;font-weight:400">Find out what solar can do for you</h2>
  <p class="abs" style="left:0;top:118px;width:1200px;text-align:center;color:var(--white);font-family:'PT Serif',serif;font-size:16px">Get a FREE customized Quote For your Home or Business!</p>
  <div class="field active" style="left:76px;top:174px;width:292px">Name *</div>
  <div class="field" style="left:380px;top:174px;width:290px">Phone *</div>
  <div class="field" style="left:682px;top:174px;width:290px">Commercial*</div>
  <div class="field" style="left:76px;top:236px;width:292px">Email *</div>
  <div class="field" style="left:380px;top:236px;width:290px">Postcode *</div>
  <div class="field" style="left:682px;top:236px;width:290px">Message *</div>
  <div class="abs" style="left:984px;top:174px;width:139px;height:112px;border:2px solid var(--white);border-radius:6px;display:flex;align-items:center;justify-content:center;color:var(--white);font-family:'PT Serif',serif;font-weight:700;font-size:18px">SUBMIT</div>
</section>

<!-- Partners -->
<section class="partners">
  <div class="abs" style="left:170px;top:3532px;width:160px;height:50px;background:#e6f2e6;border-radius:4px"></div>
  <div class="abs" style="left:368px;top:3530px;width:200px;height:54px;background:#e4eaf5;border-radius:4px"></div>
  <div class="abs" style="left:610px;top:3532px;width:82px;height:50px;background:#f7e1e3;border-radius:25px"></div>
  <div class="abs" style="left:742px;top:3530px;width:162px;height:54px;background:#fdeedd;border-radius:4px"></div>
  <div class="abs" style="left:953px;top:3530px;width:74px;height:54px;background:#e2e8f5"></div>
  <div class="abs" style="left:76px;top:3640px;width:1048px;height:1px;background:#e6e6e6"></div>
</section>

<!-- Packages -->
<section class="packages">
  <h2 class="abs heading" style="left:0;top:3696px;width:1200px;text-align:center;font-size:33px;line-height:46px;font-weight:400">Hey Queensland save over <em>$1,800/year*</em> with<br>a <em>6.6 solar</em> system from your bills !</h2>
  <div class="card" style="left:243px">
    <div class="top">BEST VALUED<br>PACKAGE</div>
    <div class="badge"></div>
    <p class="desc" style="top:210px">Built with world-class materials and top-quality installation, this extremely affordable solar package is perfect for those who want the quickest possible pay back and want to experience the cost-saving benefits of a solar energy system.</p>
    <ul style="top:420px"><li>6.6kW Solar System -<br>Fully Installed</li><li>Tier 1 Solar Panels</li><li>Voltra 5kW Inverter</li></ul>
    <div class="btn" style="left:88px;top:588px;width:166px;height:52px">Learn More</div>
  </div>
  <div class="card" style="left:612px">
    <div class="top">EUROPEAN<br>PACKAGE</div>
    <div class="badge"></div>
    <p class="desc" style="top:210px">For those who want extra quality services such as real-time monitoring for any fault-finding and generous reimbursement stipulations.</p>
    <ul style="top:376px"><li>6.6kW Solar System -<br>Fully Installed</li><li>Tier 1 Solar Panels</li><li>Helio 5kW Inverter</li></ul>
    <div class="btn" style="left:84px;top:544px;width:166px;height:52px">Learn More</div>
  </div>
</section>

<!-- Testimonial -->
<section class="testimonial">
  <div class="photo" role="img" aria-label="Red barn with solar panels on its roof and a white fence" style="left:0;top:4556px;width:1200px;height:366px;background:linear-gradient(180deg,#a9cdea,#e8f1f8 45%,#8fb86a 80%,#5e8c3e)"></div>
  <svg class="abs" style="left:500px;top:4556px" width="700" height="366" viewBox="0 0 700 366"><path d="M180 0H700V366H180L0 183Z" fill="#c41e2f"/></svg>
  <div class="photo" role="img" aria-label="Portrait of a smiling customer" style="left:580px;top:4667px;width:132px;height:132px;border-radius:50%;background:linear-gradient(160deg,#e9d6c9,#b58e78);border:4px solid var(--white)"></div>
  <div class="abs" style="left:758px;top:4630px;font-family:'PT Serif',serif;font-size:80px;color:var(--white);line-height:1">“</div>
  <p class="abs" style="left:758px;top:4710px;width:310px;font-style:italic;font-size:15px;line-height:27px;color:var(--white)">"Have been a pleasure to deal with and came up with a combinations of ideas to save money... "</p>
  <p class="abs" style="left:758px;top:4812px;color:var(--white);font-family:'PT Serif',serif;font-weight:700;font-size:15px">— &nbsp;MARIBEL</p>
  <svg class="abs" style="left:1153px;top:4690px" width="18" height="110" viewBox="0 0 18 110"><g fill="#fff"><circle cx="9" cy="9" r="6"/><circle cx="9" cy="34" r="6"/><circle cx="9" cy="59" r="5" fill="none" stroke="#fff" stroke-width="2"/><circle cx="9" cy="84" r="6"/></g></svg>
</section>

<!-- Footer -->
<footer>
  <div class="brand" style="left:115px;top:5010px"><span class="mark"></span>Torva Power</div>
  <div class="abs" style="left:178px;top:5070px;width:40px;height:40px;border-radius:50%;background:var(--red)"></div>
  <h4 class="foot-h" style="left:340px;top:4952px">Sitemap</h4>
  <ul class="foot-list" style="left:338px;top:4988px"><li>Home</li><li>Residential</li><li>Commercial</li><li>Off-Grid</li><li>Blog</li></ul>
  <h4 class="foot-h" style="left:605px;top:4952px">Get in touch</h4>
  <svg class="abs" style="left:604px;top:4992px" width="18" height="24" viewBox="0 0 18 24"><path d="M9 0a9 9 0 00-9 9c0 7 9 15 9 15s9-8 9-15a9 9 0 00-9-9z" fill="#c41e2f"/><circle cx="9" cy="9" r="3.5" fill="#fff"/></svg>
  <p class="foot-txt" style="left:638px;top:4986px">48 Wattlebird Road<br>Kingsholme QLD 4208</p>
  <svg class="abs" style="left:604px;top:5064px" width="20" height="20" viewBox="0 0 24 24"><path d="M6 2l4 5-2 2a11 11 0 007 7l2-2 5 4-2 4C10 22 2 14 2 4z" fill="#c41e2f"/></svg>
  <p class="foot-txt" style="left:638px;top:5062px">(07) 3040 8812</p>
  <svg class="abs" style="left:604px;top:5108px" width="20" height="20" viewBox="0 0 20 20"><circle cx="10" cy="10" r="8.5" fill="none" stroke="#c41e2f" stroke-width="2.5"/><path d="M10 5v5l3 2" stroke="#c41e2f" stroke-width="2" fill="none"/></svg>
  <p class="foot-txt" style="left:638px;top:5104px">Monday - Friday:<br>9:00AM - 5:00PM</p>
  <h4 class="foot-h" style="left:875px;top:4952px">Newsletter</h4>
  <p class="foot-txt" style="left:875px;top:4986px;width:245px">Would you like to receive our exclusive news &amp; update for signup our newsletter !</p>
  <div class="abs" style="left:875px;top:5084px;width:248px;height:46px;border:1px solid #ddd;font-size:13px;color:#777;padding:14px 18px">Enter Email *</div>
  <div class="abs" style="left:1082px;top:5092px;width:34px;height:30px;background:var(--red);border-radius:3px;display:flex;align-items:center;justify-content:center">
    <svg width="16" height="16" viewBox="0 0 16 16"><path d="M15 1L1 7l5 2 2 6z" fill="none" stroke="#fff" stroke-width="1.6" stroke-linejoin="round"/></svg>
  </div>
  <div class="abs" style="left:0;top:5170px;width:1200px;height:1px;background:#eee"></div>
  <p class="abs" style="left:0;top:5196px;width:1200px;text-align:center;font-size:13px;color:#777">©Torva Power - 2019 All Rights Reserved.</p>
</footer>

</body>
</html>
```